Closed loop end of life cycle for electronics Loop.

Sustainability Closed Loop. I need six sections on the Closed Loop
1-End-of-life Product & Mfg. Scrap
2-OBNE Services
3-Mechanical Processing
4-Precious Metals Refining
5-Metal Products Manufactured
6-Products return to OEMs
Target Market(s)
Vorex, Brindle, KRWP, other major manufacturers of electronics and semiconductor
Industry/Entity Type
Sustainablek
Font styles to use
Serif
Sans Serif
Colors
0054AA
0677BA
7BADD7
CADEEF
E8F1F8
0094D4
00A9DD
6FCCEA
C7EBF8
E9F6FB
00AB8E
00BBA5
67D7C9
C6EFE9
E9F9F6
Requirements
Must have
- Sustainability Closed Loop. I need six sections on the Closed Loop ring below.

```html
<!DOCTYPE html>
<html lang="en">
<head>
<meta charset="utf-8">
<title>Life Cycle for Electronics Loop</title>
<link rel="stylesheet" href="https://fonts.googleapis.com/css2?family=Roboto+Condensed:wght@700&display=swap">
<style>
  :root {
    --paper: #ffffff;
    --circuit-core: #5389a3;
    --circuit-trace: #abdeee;
    --circuit-haze: #e6f4fa;
    --chip-text: #ffffff;
    --label: #111111;
  }
  html, body {
    margin: 0;
    padding: 0;
    width: 1200px;
    height: 1200px;
    overflow: hidden;
    background: var(--paper);
  }
  .loop-diagram {
    display: block;
    width: 1200px;
    height: 1200px;
  }
  .core-stop { stop-color: var(--circuit-core); }
  .trace-stop { stop-color: var(--circuit-trace); }
  .haze-stop { stop-color: var(--circuit-haze); }
  .paper-stop { stop-color: var(--paper); }
  .stage-label, .chip-title, .chip-word {
    font-family: "Roboto Condensed", "Arial Narrow", sans-serif;
    font-weight: 700;
    text-anchor: middle;
  }
  .stage-label { fill: var(--label); font-size: 35px; }
  .stage-label.start { text-anchor: start; }
  .chip-title { fill: var(--chip-text); font-size: 42px; }
  .chip-word { fill: var(--chip-text); font-size: 92px; }
</style>
</head>
<body>
<svg class="loop-diagram" viewBox="0 0 1500 1500" xmlns="http://www.w3.org/2000/svg">
  <defs>
    <radialGradient id="circuit-fill" gradientUnits="userSpaceOnUse" cx="752" cy="768" r="720">
      <stop class="core-stop" offset="0"/>
      <stop class="core-stop" offset="0.29"/>
      <stop class="trace-stop" offset="0.34"/>
      <stop class="haze-stop" offset="0.72"/>
      <stop class="paper-stop" offset="1"/>
    </radialGradient>
  </defs>

  <rect class="circuit-art" x="30" y="70" width="1450" height="1370" fill="url(#circuit-fill)"
        role="img" aria-label="Circuit chip illustration: a square processor chip with pins on all four sides and light blue circuit traces ending in round pads radiating outward"/>

  <g class="chip-text">
    <text class="chip-title" x="750" y="727">LIFE CYCLE FOR</text>
    <text class="chip-title" x="750" y="778">ELECTRONICS</text>
    <text class="chip-word" x="754" y="880">LOOP</text>
  </g>

  <g class="stage-labels">
    <text class="stage-label" x="790" y="166">End-of-life</text>
    <text class="stage-label" x="790" y="209">Product &amp; Mfg.</text>
    <text class="stage-label" x="793" y="252">Scrap</text>

    <text class="stage-label start" x="990" y="405">OBNE Services</text>

    <text class="stage-label" x="1092" y="1000">Mechanical</text>
    <text class="stage-label" x="1096" y="1043">Processing</text>

    <text class="stage-label" x="738" y="1273">Precious Metals</text>
    <text class="stage-label" x="742" y="1316">Refining</text>

    <text class="stage-label" x="288" y="1150">Metal Products</text>
    <text class="stage-label" x="292" y="1193">Manufactured</text>

    <text class="stage-label" x="395" y="543">Products return</text>
    <text class="stage-label" x="400" y="586">to OEMs</text>
  </g>
</svg>
</body>
</html>
```